" Apoio para empresas que desejam vender produtos e/ou serviços para órgãos públicos ou empresas que utilizam processos licitatórios em suas compras "

```html
<!DOCTYPE html>
<html lang="pt-BR">
<head>
<meta charset="UTF-8">
<title>Concorra Já — Papel Timbrado</title>
<link rel="stylesheet" href="https://fonts.googleapis.com/css2?family=Cinzel:wght@600&family=Poppins:wght@400;500&display=swap">
<style>
  :root {
    --backdrop: #eef0f1;
    --paper: #ffffff;
    --navy: #1f2a4d;
    --teal: #2aa79b;
    --text-grey: #5b6270;
    --watermark: #ececec;
  }
  * { margin: 0; padding: 0; box-sizing: border-box; }
  html, body {
    width: 1200px; height: 1200px; overflow: hidden;
    background: var(--backdrop);
  }
  .letterhead {
    position: absolute;
    left: 250px; top: 48px;
    width: 703px; height: 1068px;
    background: var(--paper);
    box-shadow: 0 4px 18px rgba(0,0,0,0.12);
    overflow: hidden;
  }
  .brand {
    position: absolute; top: 62px; left: 0; right: 0;
    text-align: center;
  }
  .brand-name {
    display: inline-flex; align-items: center; gap: 12px;
    font-family: "Cinzel", serif; font-weight: 600;
    font-size: 44px; letter-spacing: 1px;
    color: var(--navy); line-height: 1;
  }
  .brand-mark {
    width: 30px; height: 30px; border-radius: 50%;
    background: var(--navy);
  }
  .brand-tagline {
    margin-top: 8px;
    font-family: "Poppins", sans-serif; font-weight: 500;
    font-size: 11px; letter-spacing: 2px;
    text-transform: uppercase; color: var(--teal);
  }
  .watermark {
    position: absolute; left: 330px; top: 330px;
    width: 440px; height: 440px; border-radius: 50%;
    background: var(--watermark);
  }
  .contact {
    position: absolute; top: 1000px; left: 20px; right: 20px;
    display: flex; gap: 60px;
    font-family: "Poppins", sans-serif; font-size: 11px;
    color: var(--text-grey); line-height: 1.9;
  }
  .contact-item { display: flex; align-items: flex-start; gap: 6px; }
  .contact-item svg { flex: none; margin-top: 4px; }
  .address { padding-left: 12px; }
  .base-band {
    position: absolute; left: 0; right: 0; bottom: 0;
    height: 14px; background: var(--teal);
  }
</style>
</head>
<body>
  <main class="letterhead">
    <header class="brand">
      <div class="brand-name"><span class="brand-mark"></span>Concorra Já</div>
      <div class="brand-tagline">Soluções em Licitações</div>
    </header>

    <div class="watermark" aria-hidden="true"></div>

    <footer class="contact">
      <div class="contact-column">
        <div class="contact-item">
          <svg width="12" height="12" viewBox="0 0 24 24" fill="none" stroke="var(--teal)" stroke-width="2.4" stroke-linecap="round" stroke-linejoin="round"><path d="M22 16.9v3a2 2 0 0 1-2.2 2 19.8 19.8 0 0 1-8.6-3.1 19.5 19.5 0 0 1-6-6A19.8 19.8 0 0 1 2.1 4.2 2 2 0 0 1 4.1 2h3a2 2 0 0 1 2 1.7c.1.9.4 1.8.7 2.7a2 2 0 0 1-.5 2.1L8 9.8a16 16 0 0 0 6 6l1.3-1.3a2 2 0 0 1 2.1-.4c.9.3 1.8.6 2.7.7a2 2 0 0 1 1.7 2z"/></svg>
          <span>(11) 90000-1234 | (11) 90000-5678</span>
        </div>
        <div class="contact-item">
          <svg width="12" height="12" viewBox="0 0 24 24" fill="none" stroke="var(--teal)" stroke-width="2.4" stroke-linejoin="round"><rect x="2" y="4" width="20" height="16" rx="2"/><path d="M2 6l10 7 10-7"/></svg>
          <span>contato@concorraja.com.br</span>
        </div>
      </div>
      <div class="contact-column">
        <div class="contact-item">
          <svg width="12" height="12" viewBox="0 0 24 24" fill="none" stroke="var(--teal)" stroke-width="2.4"><path d="M12 22s7-6.6 7-12a7 7 0 0 0-14 0c0 5.4 7 12 7 12z"/><circle cx="12" cy="10" r="2.5"/></svg>
          <span>Avenida das Palmeiras, 450 - 8º Andar</span>
        </div>
        <div class="address">Torre Ipê - Centro, Barueri - SP 06400-000</div>
      </div>
    </footer>

    <div class="base-band"></div>
  </main>
</body>
</html>
```